R.T.Pell Logging Web design

Our website needs a redesign. We want it to appear professional and easy to navigate. We will be adding videos and pictures to the new website. We do not sell any products on our website. It should be designed for informational purposes. Our company performs timber harvesting and forest management services. Attached is our new company logo.

www.rtpelllogging-example.com if you want to see our current website.

Industry/Entity Type

Graphic Design

Coding

Coded - Design and coding required

```html
<!DOCTYPE html>
<html lang="en">
<head>
<meta charset="utf-8">
<title>R.T. Pell Logging Company</title>
<link href="https://fonts.googleapis.com/css2?family=Nunito+Sans:wght@300;400;600;700&display=swap" rel="stylesheet">
<style>
:root{
  --gold:#e1a43a;
  --gold-dark:#c98b22;
  --wood:#a8662a;
  --wood-dark:#7e4616;
  --brown:#6b3a12;
  --text:#555;
  --heading:#444;
  --line:#dcdcdc;
  --white:#fff;
}
*{box-sizing:border-box;margin:0;padding:0}
html,body{width:1175px;height:1200px;overflow:hidden}
body{position:relative;font-family:"Nunito Sans",sans-serif;color:var(--text);
  background:linear-gradient(180deg,#cfe0ef 0%,#e9dcc4 20%,#d9b98a 40%,#f2ebe0 70%,#fff 85%);}
.top-line{position:absolute;left:0;top:0;width:100%;height:4px;background:var(--gold)}
.page{position:absolute;left:59px;top:4px;width:1057px;height:1089px;background:var(--white)}
.abs{position:absolute}
.brand{left:75px;top:41px;display:flex;align-items:center;gap:8px}
.brand-mark{width:34px;height:34px;background:var(--wood)}
.brand-name{color:var(--brown);font-weight:700;font-size:17px;line-height:1.05;letter-spacing:.3px}
.call{left:886px;top:30px;display:flex;gap:10px}
.call-label{font-size:18px;color:var(--heading);line-height:1.2}
.call-number{font-size:25px;color:var(--heading);line-height:1.1}
.nav{left:72px;top:95px;width:1031px;height:41px;
  background:linear-gradient(180deg,#b87533,#9c5a20 50%,#a86629);display:flex;align-items:center;
  box-shadow:0 6px 8px -4px rgba(0,0,0,.25)}
.nav a{color:var(--white);text-decoration:none;font-size:12.5px;letter-spacing:.3px;height:41px;line-height:41px;padding:0 27px}
.nav a.active{background:var(--gold);color:var(--brown);padding:0 26px}
.connect{margin-left:auto;display:flex;align-items:center;gap:7px;padding-right:11px}
.connect span{color:var(--gold);font-size:12px;margin-right:4px}
.connect i{display:block;width:29px;height:29px;border-radius:50%;background:#3b6fb0}
.connect i:last-child{background:#3a3a3a}
.slider{left:72px;top:145px;width:1031px;height:354px;background:#e4e4e4;padding:5px}
.slide{width:100%;height:100%;background:linear-gradient(100deg,#a77a46 0%,#6b6a3a 40%,#3c4a28 60%,#c9a23a 80%,#5c4a2c 100%)}
.dots{left:536px;top:462px;width:103px;height:32px;background:rgba(40,30,20,.85);display:flex;justify-content:center;align-items:center;gap:7px}
.dots i{width:11px;height:11px;border-radius:50%;background:var(--white)}
.dots i:first-child{background:var(--gold)}
h2{font-weight:400;font-size:22px;line-height:26px;color:var(--heading)}
h2 em{font-style:normal;color:var(--brown)}
.welcome{left:72px;top:534px;width:410px}
.welcome p{margin-top:13px;font-size:12.5px;line-height:20.8px;font-weight:300;color:#444}
.vline{left:501px;top:540px;width:1px;height:197px;background:var(--line)}
.services{left:525px;top:534px}
.arrows{left:1050px;top:548px}
.service-img{left:526px;top:602px;width:202px;height:135px;background:linear-gradient(180deg,#9fb3c4 0%,#6c7a5a 45%,#8a6a48 100%)}
.service-body{left:750px;top:596px;width:340px}
.service-body h3{font-weight:400;font-size:17px;color:var(--heading)}
.service-body p{margin-top:8px;font-size:12.5px;line-height:21px;font-weight:300;color:#444}
.btn{left:750px;top:701px;width:102px;height:33px;background:var(--gold);color:var(--white);font-size:14px;line-height:33px;text-align:center}
.hline{left:72px;top:768px;width:1031px;height:1px;background:var(--line)}
.video-title{left:72px;top:790px}
.pics-title{left:525px;top:790px}
.video{left:72px;top:832px;width:414px;height:229px;background:linear-gradient(170deg,#4a5a5a 0%,#3f4a32 40%,#7a5a3e 75%,#5a4632 100%)}
.play{left:248px;top:917px}
.pic{width:185px;height:108px}
.p1{background:linear-gradient(160deg,#7c8f5a,#3e5a2e)}
.p2{background:linear-gradient(160deg,#b8c4c8,#6a6a48)}
.p3{background:linear-gradient(160deg,#4e5a4a,#8a7a62)}
.p4{background:linear-gradient(160deg,#3e5a2a,#6a7a3a)}
.p5{background:linear-gradient(160deg,#3a4a6a,#b06a3a)}
.p6{background:linear-gradient(160deg,#6a7a5a,#4a5a3a)}
.footer{left:0;top:1093px;width:1175px;height:107px;background:linear-gradient(180deg,#e0a23a,#e8b14a);text-align:center;color:var(--brown)}
.footer nav{margin-top:24px;font-size:12px;letter-spacing:.3px}
.footer nav a{color:var(--brown);text-decoration:none}
.footer nav b{font-weight:400;margin:0 16px}
.footer p{font-size:11px;line-height:17px;margin-top:8px}
.footer p+p{margin-top:0}
</style>
</head>
<body>
<div class="top-line"></div>
<div class="page"></div>

<div class="abs brand"><div class="brand-mark"></div><div class="brand-name">R.T. PELL<br>LOGGING COMPANY</div></div>

<div class="abs call">
  <svg width="38" height="44" viewBox="0 0 38 44"><path d="M8 4c-4 2-6 6-5 11 2 9 9 19 17 24 4 3 8 2 11-1l-6-8-5 3c-4-3-8-9-9-13l5-3-5-10z" fill="#c8281e"/><ellipse cx="22" cy="42" rx="14" ry="2" fill="#ccc"/></svg>
  <div><div class="call-label">Call Us at:</div><div class="call-number">(555) 014-2870</div></div>
</div>

<nav class="abs nav">
  <a class="active">HOME</a><a>ABOUT US</a><a>SERVICES</a><a>GALLERY</a><a>LOCATION</a><a>CONTACT US</a>
  <div class="connect"><span>CONNECT US:</span><i></i><i></i><i></i><i></i></div>
</nav>

<div class="abs slider"><div class="slide" role="img" aria-label="Tracked excavator loading a pile of cut logs at a forest clearing"></div></div>
<div class="abs dots"><i></i><i></i><i></i><i></i></div>

<section class="abs welcome">
  <h2>Welcome to<br><em>R.T. Pell Logging Company</em></h2>
  <p>Receive high-quality professional logging and land clearing services, from R.T. Pell Logging Company based in Pine Hollow, TX. Whether your tract is large or small, our team of experts can provide the resources and solutions you need to get the job done right. Our track record for consistency, timely service, and expertise will continue to keep us competitive in the East Texas timber industry. We pay top dollar for your pine and hardwood timber.</p>
</section>
<div class="abs vline"></div>

<h2 class="abs services">Our<br><em>Services</em></h2>
<svg class="abs arrows" width="56" height="26" viewBox="0 0 56 26"><path d="M14 2L3 13l11 11M42 2l11 11-11 11" fill="none" stroke="#999" stroke-width="2"/></svg>
<div class="abs service-img" role="img" aria-label="Log truck loaded with timber at a harvest site in the hills"></div>
<div class="abs service-body">
  <h3>Timber Harvesting</h3>
  <p>Aliquam molestie, mi et imperdiet euismod, dui purus auctor tellus, et interdum lacus lectus et ante. Sed accumsan sollicitudin sapien, sit amet adipiscing turpis gravida ac.</p>
</div>
<div class="abs btn">Read More</div>

<div class="abs hline"></div>

<h2 class="abs video-title">Watch <em>Video</em></h2>
<h2 class="abs pics-title">Our <em>Pictures</em></h2>

<div class="abs video" role="img" aria-label="Video still of cut logs in front of forestry machines"></div>
<svg class="abs play" width="62" height="62" viewBox="0 0 62 62"><circle cx="31" cy="31" r="29" fill="none" stroke="#fff" stroke-width="3"/><path d="M24 17l20 14-20 14z" fill="#fff"/></svg>

<div class="abs pic p1" style="left:526px;top:832px" role="img" aria-label="Forester measuring a large tree"></div>
<div class="abs pic p2" style="left:722px;top:832px" role="img" aria-label="Crew clearing fallen timber"></div>
<div class="abs pic p3" style="left:918px;top:832px" role="img" aria-label="Harvester machine beside stacked logs"></div>
<div class="abs pic p4" style="left:526px;top:953px" role="img" aria-label="Foresters marking trees in dense woods"></div>
<div class="abs pic p5" style="left:722px;top:953px" role="img" aria-label="Forest road at sunrise"></div>
<div class="abs pic p6" style="left:918px;top:953px" role="img" aria-label="Team inspecting a forwarder in the woods"></div>

<footer class="abs footer">
  <nav><a>HOME</a><b>//</b><a>ABOUT US</a><b>//</b><a>SERVICES</a><b>//</b><a>GALLERY</a><b>//</b><a>LOCATIONS</a><b>//</b><a>CONTACT US</a></nav>
  <p>Copyright © 2014 Company Name. All Right Reserved</p>
  <p>Term of Services</p>
</footer>
</body>
</html>
```